Quiet Harbor Hours Podcast Artwork

I need a cover for my podcast Quiet Harbor Hours that is clean, modern, and minimalist, but not too feminine

Target Market(s)

People struggling with fertility particularly women who are between the ages of 35-45 though there is a small set of listeners who are men

Requirements
Must have
• Embryo in the Zero
Should not have
• No script text

```html
<!DOCTYPE html>
<html lang="en">
<head>
<meta charset="utf-8">
<title>Quiet Harbor Hours Podcast Cover</title>
<link href="https://fonts.googleapis.com/css2?family=Oswald:wght@300;500;700&display=swap" rel="stylesheet">
<style>
  :root {
    --page: #e9e7e4;
    --cover-dark: #7a5846;
    --cover-mid: #8c6c57;
    --cover-light: #a58a73;
    --cream: #fbe8df;
    --sage: #9fb597;
    --outline: rgba(251, 232, 223, 0.26);
    --photo-warm: #b3a08f;
    --photo-pale: #e4dfd8;
    --photo-cool: #6f7f92;
  }
  * { margin: 0; padding: 0; box-sizing: border-box; }
  html, body {
    width: 1200px;
    height: 807px;
    overflow: hidden;
    background: var(--page);
  }
  .podcast-cover {
    position: absolute;
    left: 250px;
    top: 53px;
    width: 700px;
    height: 700px;
    overflow: hidden;
    background: linear-gradient(120deg, var(--cover-dark) 0%, var(--cover-mid) 55%, var(--cover-light) 100%);
    box-shadow: 0 14px 30px rgba(0, 0, 0, 0.25);
  }
  .echo-rows {
    position: absolute;
    left: 28px;
    top: 0;
    font-family: "Oswald", sans-serif;
    font-weight: 700;
    font-size: 78px;
    line-height: 90px;
    letter-spacing: 2px;
    color: transparent;
    -webkit-text-stroke: 1px var(--outline);
    white-space: nowrap;
    text-transform: uppercase;
    transform: skewX(-10deg);
  }
  .echo-row { display: block; }
  .host-photo {
    position: absolute;
    left: 392px;
    top: 140px;
    width: 308px;
    height: 560px;
    border-radius: 140px 0 0 0;
    background: linear-gradient(180deg, var(--photo-warm) 0%, var(--photo-pale) 35%, var(--photo-pale) 55%, var(--photo-cool) 75%, var(--photo-pale) 100%);
    opacity: 0.85;
  }
  .cover-title {
    position: absolute;
    left: 52px;
    top: 150px;
    width: 440px;
    font-family: "Oswald", sans-serif;
    font-weight: 700;
    color: var(--cream);
    text-transform: uppercase;
    transform: skewX(-8deg);
    text-shadow: 4px 6px 10px rgba(60, 35, 25, 0.45);
  }
  .title-top {
    display: block;
    font-size: 168px;
    line-height: 0.9;
    letter-spacing: -1px;
  }
  .title-middle {
    display: block;
    margin: 8px 0 6px 112px;
    font-weight: 500;
    font-size: 50px;
    line-height: 1;
    letter-spacing: 10px;
    color: var(--sage);
    text-shadow: 2px 3px 6px rgba(60, 35, 25, 0.35);
  }
  .title-bottom {
    display: block;
    font-size: 128px;
    line-height: 0.95;
    letter-spacing: 1px;
  }
  .embryo-zero {
    position: relative;
    display: inline-block;
  }
  .embryo-zero::after {
    content: "";
    position: absolute;
    left: 50%;
    top: 55%;
    width: 22px;
    height: 30px;
    transform: translate(-50%, -50%);
    border-radius: 50%;
    background: var(--sage);
    box-shadow: 0 0 0 3px var(--cream), 0 0 0 5px var(--sage);
  }
</style>
</head>
<body>
  <main class="podcast-cover">
    <div class="echo-rows" aria-hidden="true">
      <span class="echo-row">Quiet Harbor</span>
      <span class="echo-row">Quiet Harbor</span>
      <span class="echo-row">Quiet Harbor</span>
      <span class="echo-row">Quiet Harbor</span>
      <span class="echo-row">Quiet Harbor</span>
      <span class="echo-row">Quiet Harbor</span>
      <span class="echo-row">Quiet Harbor</span>
      <span class="echo-row">Quiet Harbor</span>
    </div>
    <div class="host-photo" role="img" aria-label="Photo of a man in a white t-shirt and jeans sitting on a bed edge, head resting in his hands"></div>
    <h1 class="cover-title">
      <span class="title-top">Quiet</span>
      <span class="title-middle">Harbor</span>
      <span class="title-bottom">H<span class="embryo-zero">O</span>urs</span>
    </h1>
  </main>
</body>
</html>
```